Heronby Mortgage Capital Business Card

We need a business card design for our mortgage servicing company. In addition to servicing the loans of homeowners, we help homeowners with purchasing their homes and any mortgage refinancing. We would like to see designs that use the colors in the logo attached below (gold-ish yellow and navy blue), and any other design you deem fit! The design should communicate a simpler life with smart mortgages provided by Heronby.

```html
<!DOCTYPE html>
<html lang="en">
<head>
<meta charset="utf-8">
<title>Heronby Mortgage Capital – Business Card</title>
<link rel="stylesheet" href="https://fonts.googleapis.com/css2?family=Montserrat:wght@300;400;700&display=swap">
<style>
  :root {
    --navy: #272153;
    --gold: #e0b13c;
    --paper: #ffffff;
    --backdrop: #ececec;
  }
  * { box-sizing: border-box; margin: 0; padding: 0; }
  html, body {
    width: 1200px; height: 1200px; overflow: hidden;
    background: var(--backdrop);
    font-family: "Montserrat", sans-serif;
  }
  .card {
    position: absolute;
    left: 180px;
    width: 840px; height: 494px;
    background: var(--paper);
    overflow: hidden;
  }
  .card--front { top: 72px; }
  .card--back { top: 634px; }
  .card__shapes { position: absolute; inset: 0; width: 840px; height: 494px; }
  .navy { fill: var(--navy); }
  .gold { fill: var(--gold); }

  .wordmark {
    position: absolute;
    transform: translate(-50%, -50%);
    white-space: nowrap;
    font-weight: 700;
    color: var(--navy);
    letter-spacing: 0.5px;
  }
  .card--front .wordmark { left: 266px; top: 175px; font-size: 34px; }
  .card--back .wordmark { left: 420px; top: 247px; font-size: 46px; }

  .person {
    position: absolute; right: 50px; top: 62px; text-align: right;
  }
  .person__name {
    font-size: 27px; font-weight: 700; letter-spacing: 1px;
    color: var(--navy); text-transform: uppercase; line-height: 1.2;
  }
  .person__surname { color: var(--gold); }
  .person__role {
    font-size: 19px; font-weight: 400; color: var(--navy);
    letter-spacing: 0.5px; margin-top: 4px;
  }

  .contact {
    position: absolute; right: 46px; top: 270px;
    list-style: none; color: #fff; text-align: right;
    font-size: 20px; font-weight: 300; letter-spacing: 0.4px;
  }
  .contact__item {
    display: flex; justify-content: flex-end; align-items: flex-start;
    gap: 14px; line-height: 32px;
  }
  .contact__item--address { margin-top: 33px; line-height: 27px; }
  .contact__icon { width: 18px; height: 18px; margin-top: 7px; flex: none; }
  .contact__icon * { fill: none; stroke: #fff; stroke-width: 1.6; stroke-linecap: round; stroke-linejoin: round; }
</style>
</head>
<body>

<section class="card card--front" aria-label="Business card front">
  <svg class="card__shapes" viewBox="0 0 840 494" aria-hidden="true">
    <polygon class="navy" points="370,265 605,141 840,268 840,494 370,494"/>
    <polygon class="navy" points="0,427 157,339 315,424 315,494 0,494"/>
    <polygon class="gold" points="315,300 384,340 384,419 315,458 246,419 246,340"/>
  </svg>

  <div class="wordmark">Heronby Mortgage</div>

  <div class="person">
    <p class="person__name">Delia <span class="person__surname">Varnholt</span></p>
    <p class="person__role">Owner</p>
  </div>

  <ul class="contact">
    <li class="contact__item">
      <span>5555 555 404</span>
      <svg class="contact__icon" viewBox="0 0 18 18" aria-hidden="true"><path d="M4 2h3l1.5 4-2 1.5a9 9 0 0 0 4 4l1.5-2 4 1.5v3a2 2 0 0 1-2 2A13 13 0 0 1 2 4a2 2 0 0 1 2-2z"/></svg>
    </li>
    <li class="contact__item">
      <span>delia@heronbymortgage.com</span>
      <svg class="contact__icon" viewBox="0 0 18 18" aria-hidden="true"><rect x="2" y="4" width="14" height="10"/><path d="M2 4l7 6 7-6"/></svg>
    </li>
    <li class="contact__item">
      <span>www.heronbymortgage.com</span>
      <svg class="contact__icon" viewBox="0 0 18 18" aria-hidden="true"><circle cx="9" cy="9" r="7"/><ellipse cx="9" cy="9" rx="3" ry="7"/><path d="M2 9h14"/></svg>
    </li>
    <li class="contact__item contact__item--address">
      <span>2400 W Canyon Ridge Rd, Suite 4<br>Mesa Verde, AZ 85310</span>
      <svg class="contact__icon" viewBox="0 0 18 18" aria-hidden="true"><path d="M9 16s-5-5-5-9a5 5 0 0 1 10 0c0 4-5 9-5 9z"/><circle cx="9" cy="7" r="1.8"/></svg>
    </li>
  </ul>
</section>

<section class="card card--back" aria-label="Business card back">
  <svg class="card__shapes" viewBox="0 0 840 494" aria-hidden="true">
    <polygon class="navy" points="795,-16 873,29 873,119 795,164 717,119 717,29"/>
    <polygon class="gold" points="665,24 719,55 719,117 665,148 611,117 611,55"/>
    <polygon class="navy" points="0,424 61,389 122,421 122,494 0,494"/>
    <polygon class="gold" points="139,387 168,404 168,438 139,455 110,438 110,404"/>
  </svg>

  <div class="wordmark">Heronby Mortgage</div>
</section>

</body>
</html>
```